Mobile Optometry needs descriptive brochure and business cards for patients

I need a brochure design and business cards for a new optometry service that brings full ocular examination, refraction, and spectacle dispensing to the patient in need.
I will mainly be working out of senior homes so it needs to be very legible NO SMALL PRINT, CLEAR, CONSCIENCE.
The final design needs to incorporate the logo and colouring that was just selected from a previous project. I will add this file as soon as I get the final changes back from the designer.

Here is what I would like in the broacher. I don't have a fax number, website address, email address set up yet but have room for this.

Note: I have attached the logo I selected for the company. I may not have attached the most detailed version but this will give you an idea of colouring and style. I will upload the proper image soon.

Routine eye examinations are crucial for early detection of diseases of the eye and effects of systemic conditions for everybody. As we age we are at higher risk of vision loss due to Glaucoma, Age-related Macular Degeneration, Diabetic or Hypertensive Retinopathy, Cataracts and many other diseases.

During your complete ocular visual assessment you will be screened for all conditions that may be affecting you as well as treat any issues you may be suffering from. Common treatable complaints: Dry eyes, Watery eyes, Burning, Itching, Difficulty reading small print, Reduced distance vision, Glare, Light sensitiveness, and difficulty performing hobbies.

Here is what your complete examination includes

Step 1: Appointment Request
-Call
-Email
-Phone
-Fax

Step 2: Welcome form
-Patient Name, DOB, QR Wellcover number
-List current medications, allergies
-Current Visual difficulties
-Previous spectacle prescription (if available)

Step 3: Ocular Visual Assessment and Discussion of Results
-History & Symptoms
-Refraction
-Dilation and thorough ocular/retinal screening
-Spectacle or magnifier dispense if required
-Ophthalmologist or medical practitioner referral if required

Step 4: Dispense and Delivery
-Return to fit custom made glasses
-Demonstrate use low vision device
-Discuss any questions/treatments/referrals

I have just increased the budget. I am running out of time and want some good designs. I want a modern, clean and clear product. Please submit, points for originality.

Target Market(s)

The target audience is Professionals, managers, senior care facilities, families. I want something clean and easy to read. I want something modern but not trendy and something that appeals to the masses.

Industry/Entity Type

Medical

Font styles to use
Sans Serif

Requirements
Must have
• easy to read
bright
professional
Contact information on the last page
Nice to have
• order of services layer out nicely. Try a version with clearly defined steps. Step 1. Step 2. Step 3. Could be multiple broachers that are packaged together.
Should not have
• cartoony
serif fonts (please use font that is in logo)

```html
<!DOCTYPE html>
<html lang="en">
<head>
<meta charset="utf-8">
<title>AB Health Care – Brochure Cover</title>
<link rel="stylesheet" href="https://fonts.googleapis.com/css2?family=Open+Sans:wght@400;600&family=Montserrat:wght@400&display=swap">
<style>
  :root {
    --green: #97cb45;
    --yellow: #ecea55;
    --yellow-soft: #f3ef6e;
    --white: #ffffff;
    --ink: #3b3b3d;
    --skin: #f1d9d6;
    --skin-deep: #d9a79b;
    --iris: #8a5a3a;
  }
  html, body {
    margin: 0;
    padding: 0;
    overflow: hidden;
    background: var(--white);
  }
  .brochure {
    position: relative;
    width: 1200px;
    height: 927px;
    overflow: hidden;
    font-family: "Open Sans", sans-serif;
  }
  .panel {
    position: absolute;
    top: 0;
    width: 600px;
    height: 927px;
    overflow: hidden;
  }
  .panel--back { left: 0; background: var(--white); }
  .panel--front { left: 600px; background: var(--green); }
  .panel-art {
    position: absolute;
    inset: 0;
  }
  .brand {
    position: absolute;
    left: 0;
    width: 600px;
    text-align: center;
  }
  .brand__name {
    margin: 0;
    font-weight: 600;
    color: var(--ink);
    letter-spacing: -0.3px;
    line-height: 1;
  }
  .brand__tagline {
    margin: 10px 0 0;
    font-weight: 400;
    color: var(--ink);
    letter-spacing: 1px;
  }
  .panel--back .brand { top: 278px; }
  .panel--back .brand__name { font-size: 30px; }
  .panel--back .brand__tagline { font-size: 14px; }

  .panel--front .brand { top: 205px; left: 5px; }
  .panel--front .brand__name { font-size: 37px; }
  .panel--front .brand__tagline { font-size: 17px; margin-top: 12px; }

  .contact {
    position: absolute;
    top: 786px;
    left: 0;
    width: 600px;
    margin: 0;
    text-align: center;
    font-family: "Montserrat", sans-serif;
    font-size: 20px;
    line-height: 27.5px;
    color: var(--white);
  }
  .website {
    position: absolute;
    top: 879px;
    left: 0;
    width: 600px;
    margin: 0;
    text-align: center;
    font-family: "Montserrat", sans-serif;
    font-size: 15px;
    color: var(--white);
  }
</style>
</head>
<body>
<main class="brochure">

  <section class="panel panel--back">
    <svg class="panel-art" width="600" height="927" viewBox="0 0 600 927" aria-hidden="true">
      <path d="M0 400 C 160 455, 300 470, 420 445 C 500 428, 560 390, 600 335 L600 927 L0 927 Z" fill="var(--yellow)"/>
      <path d="M0 425 C 150 470, 300 485, 430 465 C 510 450, 570 410, 600 370 L600 927 L0 927 Z" fill="var(--white)"/>
      <path d="M0 432 C 160 478, 320 492, 450 475 C 520 465, 575 430, 600 395 L600 927 L0 927 Z" fill="var(--green)"/>
    </svg>

    <div class="brand">
      <h2 class="brand__name">AB Health Care</h2>
      <p class="brand__tagline">MOBILE OPTOMETRY</p>
    </div>

    <p class="contact">
      Address: 48 Harbour Lane, Unit 2<br>
      Contact Numbers: (555) 014 2287<br>
      Email: hello@abhealth.example
    </p>
  </section>

  <section class="panel panel--front">
    <svg class="panel-art" width="600" height="927" viewBox="0 0 600 927">
      <defs>
        <radialGradient id="photo-tone" cx="0.58" cy="0.58" r="0.55">
          <stop offset="0" stop-color="var(--iris)" stop-opacity="0.85"/>
          <stop offset="0.22" stop-color="var(--skin-deep)" stop-opacity="0.75"/>
          <stop offset="0.6" stop-color="var(--skin)" stop-opacity="0.7"/>
          <stop offset="1" stop-color="var(--white)" stop-opacity="0"/>
        </radialGradient>
        <clipPath id="cover-window">
          <path d="M0 195 C 150 95, 380 65, 600 95 L600 690 C 480 800, 300 840, 0 770 Z"/>
        </clipPath>
      </defs>
      <path d="M0 180 C 150 70, 380 40, 600 80 L600 150 C 420 75, 190 80, 0 205 Z" fill="var(--yellow-soft)"/>
      <path d="M0 195 C 150 95, 380 65, 600 95 L600 690 C 480 800, 300 840, 0 770 Z" fill="var(--white)"/>
      <g clip-path="url(#cover-window)">
        <rect x="0" y="270" width="600" height="560" fill="url(#photo-tone)"
              role="img" aria-label="Close-up photograph of a brown eye with long lashes, softly fading into white"/>
      </g>
      <path d="M0 770 C 300 840, 480 800, 600 690 L600 720 C 470 830, 300 860, 0 790 Z" fill="var(--yellow)"/>
      <path d="M0 790 C 300 860, 470 830, 600 720 L600 735 C 470 845, 300 875, 0 805 Z" fill="var(--white)"/>
    </svg>

    <div class="brand">
      <h1 class="brand__name">AB Health Care</h1>
      <p class="brand__tagline">MOBILE OPTOMETRY</p>
    </div>

    <p class="website">www.abhealth.example</p>
  </section>

</main>
</body>
</html>
```